Creation of an E Book on Business Risk

I have the Copy... I would like this copy to be made into an interesting ebook - with Pictures that are relevant to the topic.

You also need to include the Quill Logo's and Colour schemes as per attached other brochures

Hi
I am looking for the same theme as the previous ebook "steps to grow savings through your trust fund"

HEADING PAGE
How to protect your business from risk

with a picture that portrays the sentence

PART 2 Disclaimer and contents
clean and simple
(same as

PART 3 Bsns is Personal anfd ... family's future..

PART 4 Buy Sell and Case Studies

etc...

Each Part should have an awesome Picture that relates to the subject

thanks
Dorin

Target Market(s)

Small to Medium Size Businesses that need to protect themselves from unforeseen events

Industry/Entity Type

Business

Requirements
Must have
• THe Brochure must have all the copy, and flow with pictures that are relevant to the theme

```html
<!DOCTYPE html>
<html lang="en">
<head>
<meta charset="utf-8">
<title>5. Tax &amp; Structure</title>
<link rel="stylesheet" href="https://fonts.googleapis.com/css2?family=Roboto:wght@300;400;700;900&display=swap">
<style>
  :root {
    --brand-blue: #1b9ad8;
    --brand-navy: #23306e;
    --body-grey: #8c8c8c;
    --rule-blue: #a9d6ee;
    --paper: #ffffff;
    --sky-top: #1a3f86;
    --sky-mid: #2f6fb8;
    --glass-light: #9cc8ea;
  }
  * { margin: 0; padding: 0; box-sizing: border-box; }
  html, body { width: 1200px; height: 849px; overflow: hidden; background: var(--paper); }
  body { font-family: "Roboto", Arial, sans-serif; position: relative; }

  .spread { position: relative; width: 1200px; height: 849px; overflow: hidden; }

  .edge-photo {
    position: absolute; left: 0; top: 0; width: 32px; height: 849px;
    background: linear-gradient(180deg, #c9cfd6 0%, #a7b3c0 30%, #d9c7a4 60%, #ecd9b0 100%);
  }
  .page-left { position: absolute; left: 32px; top: 0; width: 568px; height: 849px; background: var(--paper); }

  .corner-tab { position: absolute; left: 73px; top: 0; width: 40px; height: 80px; background: var(--brand-blue); }

  .title { position: absolute; left: 73px; top: 92px; width: 420px; height: 190px; color: var(--brand-blue); font-weight: 900; line-height: 1; }
  .title span { position: absolute; white-space: nowrap; }
  .title .num { left: 62px; top: 44px; font-size: 44px; letter-spacing: -2px; }
  .title .tax { left: 103px; top: 0; font-size: 100px; letter-spacing: -7px; }
  .title .amp { left: 258px; top: 42px; font-size: 46px; }
  .title .structure { left: 0; top: 72px; font-size: 106px; letter-spacing: -7px; }
  .title .reflection {
    left: 0; top: 72px; font-size: 106px; letter-spacing: -7px;
    transform-origin: 0 88%; transform: scaleY(-0.42); opacity: 0.16;
    -webkit-mask-image: linear-gradient(0deg, transparent 0%, #000 100%);
            mask-image: linear-gradient(0deg, transparent 0%, #000 100%);
  }

  .body-copy { position: absolute; left: 73px; top: 312px; width: 470px; color: var(--body-grey); font-size: 10.4px; line-height: 18px; font-weight: 400; }
  .body-copy p { margin-bottom: 13px; }
  .body-copy em { font-style: normal; color: var(--brand-blue); font-weight: 700; }

  .advice-wheel { position: absolute; left: 0; top: 0; }

  .footer-rule { position: absolute; left: 73px; top: 793px; width: 1057px; height: 1px; background: var(--rule-blue); }
  .brand-mark { position: absolute; left: 75px; top: 800px; display: flex; align-items: center; gap: 6px; color: var(--brand-blue); font-size: 12px; font-weight: 300; }
  .brand-mark .dot { width: 14px; height: 14px; border-radius: 50%; background: var(--brand-blue); }

  .tower-photo {
    position: absolute; left: 600px; top: 0; width: 600px; height: 849px;
    background: linear-gradient(175deg, var(--sky-top) 0%, #274f9a 18%, var(--sky-mid) 45%, var(--glass-light) 70%, #3d7fc2 100%);
  }
  .site-url { position: absolute; right: 62px; top: 809px; color: #e9f3fb; font-size: 9px; }
</style>
</head>
<body>
<div class="spread">
  <div class="edge-photo" role="img" aria-label="Soft blurred photograph bleeding in from the page edge"></div>
  <div class="page-left"></div>
  <div class="corner-tab"></div>

  <h1 class="title">
    <span class="num">5.</span>
    <span class="tax">Tax</span>
    <span class="amp">&amp;</span>
    <span class="reflection" aria-hidden="true">Structure</span>
    <span class="structure">Structure</span>
  </h1>

  <div class="body-copy">
    <p>There are several strategies and ways business risk policies can be structured and funded. This can include holding the policy within your Superannuation Account.</p>
    <p>The ownership / beneficiary structure and relationship of each policy is also vital, as strategic planning and implementation could remove the potential tax liability at the time of claim.</p>
    <p>It is important to work with your financial adviser, accountant and taxation lawyer with regards to <em>how</em> and <em>when</em> these policy premiums and benefit payments are subject to tax.</p>
    <p>Some premiums will be tax deductible, however their benefit payments will be tax assessable. Others will not have a tax deductible premium, however the benefit payment will not be tax assessable.</p>
  </div>

  <svg class="advice-wheel" width="600" height="849" viewBox="0 0 600 849" aria-label="Your Business supported by accountant, financial adviser and lawyer">
    <defs>
      <radialGradient id="hub" cx="45%" cy="35%" r="70%">
        <stop offset="0" stop-color="#7fd0f5"/><stop offset="1" stop-color="#1b86c9"/>
      </radialGradient>
      <path id="arc-accountant" d="M224.6 666.3 A77 77 0 0 1 281 564.7"/>
      <path id="arc-adviser" d="M303.7 563.3 A77 77 0 0 1 369.4 666.3"/>
      <path id="arc-lawyer" d="M351.4 694.4 A77 77 0 0 1 242.6 694.4"/>
    </defs>
    <circle cx="297" cy="640" r="100" fill="#e9f1f7"/>
    <path d="M210.9 680.2 A95 95 0 0 1 288.7 545.4 L292.2 585.2 A55 55 0 0 0 247.2 663.3 Z" fill="#5aa3dd"/>
    <path d="M300.3 545.1 A95 95 0 0 1 383.1 680.2 L346.8 663.3 A55 55 0 0 0 298.9 585.1 Z" fill="var(--brand-navy)"/>
    <path d="M377.6 690.3 A95 95 0 0 1 216.4 690.3 L250.4 669.2 A55 55 0 0 0 343.6 669.2 Z" fill="#2a6dbf"/>
    <g fill="#ffffff" font-size="13" font-family="Roboto, Arial, sans-serif">
      <text><textPath href="#arc-accountant" startOffset="50%" text-anchor="middle">Accountant</textPath></text>
      <text><textPath href="#arc-adviser" startOffset="50%" text-anchor="middle">Financial Adviser</textPath></text>
      <text><textPath href="#arc-lawyer" startOffset="50%" text-anchor="middle">Lawyer</textPath></text>
    </g>
    <circle cx="297" cy="640" r="50" fill="#ffffff"/>
    <circle cx="297" cy="640" r="46" fill="url(#hub)"/>
    <g fill="#ffffff" font-size="15" font-weight="700" text-anchor="middle" font-family="Roboto, Arial, sans-serif">
      <text x="297" y="634">Your</text>
      <text x="297" y="651">Business</text>
    </g>
  </svg>

  <div class="tower-photo" role="img" aria-label="Photograph looking up a glass skyscraper with diagonal cross bracing against a blue sky"></div>

  <div class="footer-rule"></div>
  <div class="brand-mark"><span class="dot"></span><span>Quill Harbour Advisory</span></div>
  <div class="site-url">www.quillharbour.com.au</div>
</div>
</body>
</html>
```